Cedar Grove Worship Chapel CG- Theme for 2022

We, Cedar Grove Worship Chapel of Willow Bend, need a design for a 4' x 6' banner that will be placed on two walls in the main sanctuary. The banner is to communicate/advertise the church's theme for 2022, "He Will Make All Things New: A New You - 2022" Revelations 21:5. The design should include our logo and church name. Use the color purple. We have not worshipped in our church building since 2020 due to the COVID pandemic. This banner should be reflective of change, newness as we plan to re-enter the building this spring. Our congregation demographic is 95% African American, 5% Hispanic. Our home base is Tampa, Florida (USA), but we have a large social media following, primarily due to the pandemic.

Target Market(s)

Church members, Ages 1-99; male and female

Industry/Entity Type

Religious

Font styles to use
Serif

Colors
0094D4
00A9DD
6FCCEA
C7EBF8
E9F6FB
00AB8E
00BBA5
67D7C9
C6EFE9
E9F9F6
6B429C
8869AF
B7A5CE
E3DAEB
F3F0F8

Requirements
Must have
• Theme, scripture, church logo and color purple

```html
<!DOCTYPE html>
<html lang="en">
<head>
<meta charset="utf-8">
<title>He Will Make All Things New – Cedar Grove Worship Chapel</title>
<link rel="stylesheet" href="https://fonts.googleapis.com/css2?family=Poppins:wght@700;800;900&family=Libre+Baskerville&family=Arimo:wght@400;700&display=swap">
<style>
  :root {
    --purple-deep: #4a3a96;
    --purple: #6b429c;
    --purple-mid: #7d3aa0;
    --violet: #8a3aa6;
    --magenta: #b33aa8;
    --pink: #c23ca8;
    --ink: #111016;
    --white: #ffffff;
    --sun-bright: #ffd87a;
    --sun-gold: #c98a2a;
    --sun-dark: #3a2512;
  }
  html, body {
    margin: 0;
    padding: 0;
    overflow: hidden;
    background: var(--white);
  }
  .banner {
    position: relative;
    width: 1200px;
    height: 608px;
    overflow: hidden;
    background: linear-gradient(110deg, var(--purple-deep) 0%, var(--purple-mid) 45%, var(--violet) 70%, var(--magenta) 100%);
    font-family: "Poppins", sans-serif;
    color: var(--white);
  }
  .banner__shapes {
    position: absolute;
    inset: 0;
  }
  .logo {
    position: absolute;
    left: 238px;
    top: 24px;
    width: 166px;
    height: 166px;
    border-radius: 50%;
    background: var(--ink);
    display: flex;
    align-items: center;
    justify-content: center;
    text-align: center;
  }
  .logo__name {
    font-weight: 700;
    font-size: 17px;
    line-height: 1.2;
    width: 120px;
  }
  .theme {
    position: absolute;
    left: 0;
    top: 196px;
    width: 650px;
    margin: 0;
    text-align: center;
    font-weight: 800;
    font-size: 62px;
    line-height: 69px;
    letter-spacing: -1px;
  }
  .theme span { display: block; }
  .scripture {
    position: absolute;
    left: 414px;
    top: 418px;
    width: 164px;
    text-align: right;
    font-family: "Libre Baskerville", serif;
    font-size: 20px;
  }
  .social {
    position: absolute;
    left: 77px;
    top: 518px;
    display: flex;
    align-items: center;
    gap: 8px;
    font-family: "Arimo", sans-serif;
    font-size: 14px;
    font-weight: 700;
  }
  .social__dot {
    width: 24px;
    height: 24px;
    border-radius: 50%;
    background: var(--white);
  }
  .website {
    position: absolute;
    left: 77px;
    top: 550px;
    font-family: "Arimo", sans-serif;
    font-size: 22px;
  }
  .church-info {
    position: absolute;
    left: 892px;
    top: 516px;
    font-family: "Arimo", sans-serif;
    font-size: 14px;
    line-height: 18px;
  }
  .church-info__name {
    font-weight: 700;
    margin: 0;
  }
  .church-info__address { margin: 0; }
</style>
</head>
<body>
<main class="banner">
  <svg class="banner__shapes" width="1200" height="608" viewBox="0 0 1200 608">
    <defs>
      <linearGradient id="sunlight" x1="1" y1="0" x2="0" y2="1">
        <stop offset="0" stop-color="#ffe9a8"/>
        <stop offset="0.25" stop-color="#f3b24a"/>
        <stop offset="0.55" stop-color="#8a5a22"/>
        <stop offset="1" stop-color="#3a2512"/>
      </linearGradient>
      <linearGradient id="band-pink" x1="0" y1="0" x2="1" y2="1">
        <stop offset="0" stop-color="#c23ca8"/>
        <stop offset="1" stop-color="#7b3a9e"/>
      </linearGradient>
      <linearGradient id="band-right" x1="0" y1="1" x2="1" y2="0">
        <stop offset="0" stop-color="#c23ca8"/>
        <stop offset="1" stop-color="#8a3aa6"/>
      </linearGradient>
    </defs>
    <polygon class="band band--left-pink" points="0,400 0,608 520,608" fill="url(#band-pink)"/>
    <polygon class="band band--left-dark" points="0,400 750,608 460,608 0,460" fill="#5b2f88" opacity="0.75"/>
    <polygon class="band band--fold" points="522,0 760,0 750,472" fill="#9a3fb0" opacity="0.55"/>
    <polygon class="photo" role="img" aria-label="Photo of a person with open arms standing in a sunlit stone archway"
             points="522,3 1197,3 1197,259 750,472" fill="url(#sunlight)"/>
    <polygon class="band band--right" points="750,472 1200,262 1200,608 750,608" fill="url(#band-right)"/>
    <polygon class="band band--right-dark" points="750,472 1200,300 1200,608 760,608" fill="#6b3a9e" opacity="0.55"/>
  </svg>

  <div class="logo">
    <span class="logo__name">Cedar Grove Worship Chapel</span>
  </div>

  <h1 class="theme">
    <span>He Will Make</span>
    <span>All Things New</span>
    <span>A New You - 2022</span>
  </h1>
  <p class="scripture">Revelations 21:5</p>

  <div class="social">
    <span class="social__dot"></span>
    <span>Chatter · Friendbook</span>
  </div>
  <div class="website">www.cedargrovewb.org</div>

  <div class="church-info">
    <p class="church-info__name">Cedar Grove Worship Chapel of<br>Willow Bend</p>
    <p class="church-info__address">2450 Orchard Lane Tampa, FL 33610</p>
  </div>
</main>
</body>
</html>
```